Business card for Luxury Portable Restroom Trailer company

We are a Luxury Portable Restroom Trailer Company Called FALVEX HIRINGS. Based in Orange County California. We provide portable restroom trailers for events, such as, Weddings, Concerts, Charity events, Sporting events, Tournaments, Corporate events, ect. We rent and Sell the Luxury restrooms. Our colors are white, grey, and Orange. As you will see in the logo we uploaded.
There are 2 people in the company so the names and titles will change for the 3 people but card will remain the same. Here is the information for each Person: Desmond Purt CFO 555 018-3374
next Person: Milo Fenwright VP 555 018-3374
Next Person: Owen Fenwright CEO 555 018-3374
Information to include on the card: Luxury Restroom Trailers Rental and Sales. Weddings, Concerts, Charity, Sporting and Corp. Events.

```html
<!DOCTYPE html>
<html lang="en">
<head>
<meta charset="UTF-8">
<title>FALVEX HIRINGS — Business Card</title>
<link rel="stylesheet" href="https://fonts.googleapis.com/css2?family=Montserrat:wght@400;500;600;800&family=Oswald:wght@500&display=swap">
<style>
  :root {
    --orange: #f36f21;
    --ink: #1c1c1c;
    --grey-text: #3a3a3a;
    --card-dark: #474747;
    --card-light: #ffffff;
    --backdrop: #2e2e30;
  }
  * { box-sizing: border-box; margin: 0; padding: 0; }
  html, body { width: 1200px; height: 1200px; overflow: hidden; }
  body {
    background: var(--backdrop);
    font-family: "Montserrat", sans-serif;
    position: relative;
  }
  .card {
    position: absolute;
    left: 120px;
    width: 960px;
    height: 548px;
    border-radius: 40px;
    box-shadow: 0 14px 30px rgba(0,0,0,.45);
  }
  .card--front { top: 40px; background: var(--card-light); }
  .card--back  { top: 612px; background: var(--card-dark); display: flex; align-items: center; justify-content: center; }

  .contact { position: absolute; left: 78px; top: 200px; }
  .contact__name {
    color: var(--orange);
    font-weight: 600;
    font-size: 50px;
    letter-spacing: 2px;
    line-height: 1;
  }
  .contact__title {
    color: var(--grey-text);
    font-size: 34px;
    font-weight: 400;
    line-height: 1.1;
    margin-bottom: 14px;
  }
  .contact__line {
    display: flex;
    align-items: center;
    gap: 18px;
    color: var(--ink);
    font-size: 29px;
    line-height: 1.45;
  }
  .contact__icon { width: 30px; height: 30px; flex: none; }

  .brand {
    position: absolute;
    right: 120px;
    top: 60px;
    display: flex;
    flex-direction: column;
    align-items: center;
    gap: 14px;
  }
  .brand__ring {
    width: 170px; height: 170px;
    border: 14px solid var(--orange);
    border-radius: 50%;
  }
  .brand__name {
    color: var(--orange);
    font-weight: 800;
    font-size: 30px;
    letter-spacing: 2px;
  }

  .services {
    position: absolute;
    right: 60px;
    bottom: 44px;
    text-align: right;
    font-family: "Oswald", sans-serif;
    font-weight: 500;
    text-transform: uppercase;
    line-height: 1.15;
  }
  .services__headline { color: var(--orange); font-size: 36px; }
  .services__list { color: var(--ink); font-size: 33px; }
  .services__dot { color: var(--orange); }

  .back-brand {
    color: var(--orange);
    font-weight: 800;
    font-size: 84px;
    letter-spacing: 4px;
  }
</style>
</head>
<body>
  <section class="card card--front">
    <div class="brand">
      <div class="brand__ring"></div>
      <div class="brand__name">FALVEX HIRINGS</div>
    </div>

    <div class="contact">
      <div class="contact__name">DESMOND PURT</div>
      <div class="contact__title">CFO</div>
      <div class="contact__line">
        <svg class="contact__icon" viewBox="0 0 24 24"><path fill="#f36f21" d="M6.6 10.8a15 15 0 0 0 6.6 6.6l2.2-2.2c.3-.3.7-.4 1-.2 1.1.4 2.3.6 3.6.6.6 0 1 .4 1 1V20c0 .6-.4 1-1 1A17 17 0 0 1 3 4c0-.6.4-1 1-1h3.5c.6 0 1 .4 1 1 0 1.3.2 2.5.6 3.6.1.3 0 .7-.2 1z"/></svg>
        <span>555 018-3374</span>
      </div>
      <div class="contact__line">
        <svg class="contact__icon" viewBox="0 0 24 24"><rect x="2" y="5" width="20" height="14" fill="#f36f21"/><path d="M2 5l10 8 10-8" fill="none" stroke="#fff" stroke-width="1.6"/></svg>
        <span>email@falvexhire.com</span>
      </div>
      <div class="contact__line">
        <svg class="contact__icon" viewBox="0 0 24 24" fill="none" stroke="#f36f21" stroke-width="1.8"><circle cx="12" cy="12" r="10"/><ellipse cx="12" cy="12" rx="4.5" ry="10"/><path d="M2 12h20M4 7h16M4 17h16"/></svg>
        <span>www.falvexhire.com</span>
      </div>
    </div>

    <div class="services">
      <div class="services__headline">Luxury Restroom Trailers Rental and Sales.</div>
      <div class="services__list">Weddings <span class="services__dot">•</span> Concerts <span class="services__dot">•</span> Charity <span class="services__dot">•</span> Sporting and Corp. Events.</div>
    </div>
  </section>

  <section class="card card--back">
    <div class="back-brand">FALVEX HIRINGS</div>
  </section>
</body>
</html>
```